The Perfect Business Card for PineHarbor

I am looking for a business card which beautifully incorporates my logo, reflects my business and looks special, elegant and clean.

```html
<!DOCTYPE html>
<html lang="en">
<head>
<meta charset="utf-8">
<title>PineHarbor Business Card</title>
<link href="https://fonts.googleapis.com/css2?family=Alegreya:wght@400;700&family=Arimo:wght@400&display=swap" rel="stylesheet">
<style>
  :root {
    --backdrop: #b9b9b9;
    --paper: #ffffff;
    --forest: #52672e;
    --leaf: #7c9c43;
    --brand: #6a8a36;
    --ink: #1c1c1c;
    --on-dark: #ffffff;
    --mark-light: #e9efdc;
  }
  * { margin: 0; padding: 0; box-sizing: border-box; }
  html, body { width: 1075px; height: 1200px; overflow: hidden; }
  body { background: var(--backdrop); position: relative; font-family: "Arimo", Arial, sans-serif; }

  .card {
    position: absolute; left: 206px; width: 663px; height: 396px;
    box-shadow: 3px 3px 2px rgba(0,0,0,.75);
    overflow: hidden;
  }
  .card--front { top: 187px; background: var(--paper); }
  .card--back { top: 637px; background: var(--forest); }

  .brand { position: absolute; display: flex; align-items: center; gap: 14px; }
  .brand__dot { width: 110px; height: 110px; border-radius: 50%; border: 2px solid currentColor; opacity: .8; }
  .brand__name { font-family: "Alegreya", Georgia, serif; font-weight: 400; font-size: 52px; letter-spacing: .5px; line-height: 1; }
  .card--front .brand { left: 262px; top: 58px; color: var(--brand); }
  .card--back .brand { left: 132px; top: 132px; color: var(--mark-light); }
  .card--back .brand__dot { width: 130px; height: 130px; border-color: var(--leaf); }

  .person { position: absolute; left: 35px; top: 226px; }
  .person__name { font-family: "Alegreya", Georgia, serif; font-weight: 700; font-size: 21px; color: var(--forest); letter-spacing: .3px; }
  .person__name .first { color: var(--leaf); }
  .person__role { font-size: 16px; color: var(--ink); margin-top: -1px; }
  .person__rule { position: absolute; left: 35px; top: 273px; width: 205px; height: 4px; background: var(--leaf); }

  .contact-band { position: absolute; left: 0; top: 279px; width: 100%; height: 117px; background: var(--forest); color: var(--on-dark); }
  .contact-list { position: absolute; left: 35px; top: 22px; list-style: none; font-size: 17px; }
  .contact-list li { display: flex; align-items: center; gap: 6px; height: 24px; }
  .contact-list svg { width: 17px; height: 17px; fill: none; stroke: var(--on-dark); stroke-width: 1.6; }
  .address { position: absolute; right: 40px; top: 47px; text-align: right; font-size: 17px; line-height: 24px; }

  .web-band { position: absolute; left: 0; bottom: 0; width: 100%; height: 45px; background: var(--leaf); color: var(--on-dark); font-size: 17px; display: flex; align-items: center; justify-content: center; }
</style>
</head>
<body>
  <section class="card card--front">
    <div class="brand">
      <span class="brand__dot"></span>
      <span class="brand__name">PineHarbor</span>
    </div>
    <div class="person">
      <p class="person__name"><span class="first">DANIEL</span> HARWOOD</p>
      <p class="person__role">MANAGING DIRECTOR</p>
    </div>
    <div class="person__rule"></div>
    <div class="contact-band">
      <ul class="contact-list">
        <li><svg viewBox="0 0 20 20"><path d="M4 2l3 0 1.5 4-2 1.5a10 10 0 0 0 6 6l1.5-2 4 1.5 0 3a2 2 0 0 1-2 2A16 16 0 0 1 2 4a2 2 0 0 1 2-2z"/></svg>044-987 654 321</li>
        <li><svg viewBox="0 0 20 20"><rect x="2" y="4" width="16" height="12"/><path d="M2 4l8 7 8-7"/></svg>hello@pineharbor.com</li>
        <li><svg viewBox="0 0 20 20"><circle cx="10" cy="10" r="8"/><ellipse cx="10" cy="10" rx="3.5" ry="8"/><path d="M2 10h16M3.5 6h13M3.5 14h13"/></svg>www.pineharbor.com</li>
      </ul>
      <p class="address">421, Address line goes here<br>45452, Country Name</p>
    </div>
  </section>

  <section class="card card--back">
    <div class="brand">
      <span class="brand__dot"></span>
      <span class="brand__name">PineHarbor</span>
    </div>
    <div class="web-band">www.pineharbor.com</div>
  </section>
</body>
</html>
```